Modern Business Card Design Needed for Young Realtor

Information that is going on the card:Marvin Pold
Broker/Owner
555.210.3367
Marvin@MPoldRealty.com
www.MPoldRealty.com

Would also like to include my plain circle Handle somewhere. Probably on the back: the_queencity_realtorMy previous business card is attached, I like that one but would like an updated version and maybe a few design changes

Marvin Pold
Broker/Owner
555.210.3367
Marvin@MPoldRealty.com
www.MPoldRealty.com

• Would also like to include my plain circle Handle somewhere. Probably on the back: the_pinecrest_realtor
• Dorrance Hale or the DH (logo from the previous card.)

```html
<!DOCTYPE html>
<html lang="en">
<head>
<meta charset="utf-8">
<title>MPold Realty — Business Card</title>
<link rel="stylesheet" href="https://fonts.googleapis.com/css2?family=Questrial&family=Anton&display=swap">
<style>
  :root {
    --page: #e9e9ea;
    --card-black: #1b1b1c;
    --card-band: #2f2f31;
    --ink: #f2f2f2;
    --ink-soft: #cfcfcf;
    --accent: #c0202b;
    --photo-top: #6f8f4e;
    --photo-bottom: #a7a49a;
  }
  * { box-sizing: border-box; margin: 0; padding: 0; }
  html, body { width: 1200px; height: 1070px; overflow: hidden; }
  body {
    background: var(--page);
    font-family: "Questrial", "Century Gothic", sans-serif;
    color: var(--ink);
    position: relative;
  }
  .card {
    position: absolute;
    background: var(--card-black);
    border-radius: 28px;
    overflow: hidden;
    box-shadow: 0 14px 30px rgba(0,0,0,.18);
  }

  /* Front */
  .card-front { left: 80px; top: 200px; width: 380px; height: 670px; display: flex; flex-direction: column; }
  .portrait {
    height: 230px;
    flex: none;
    background: linear-gradient(160deg, var(--photo-top) 0%, #8a9a70 45%, var(--photo-bottom) 100%);
  }
  .front-brand { padding: 20px 30px 14px; }
  .brand-name {
    font-size: 24px;
    letter-spacing: 5px;
    color: var(--ink);
    text-transform: uppercase;
    white-space: nowrap;
  }
  .agent-name { margin-top: 12px; font-size: 24px; line-height: 1.15; color: var(--ink); }
  .agent-title { margin-top: 2px; font-size: 15px; letter-spacing: 1px; color: var(--accent); text-transform: uppercase; }
  .phones { margin-top: 10px; font-size: 20px; line-height: 1.3; color: var(--ink); letter-spacing: .5px; }
  .web-band { background: var(--card-band); padding: 14px 30px; font-size: 18px; line-height: 1.45; color: var(--ink); }
  .office { padding: 16px 30px 0; flex: 1; display: flex; flex-direction: column; }
  .office-title {
    font-family: "Anton", "Impact", sans-serif;
    color: var(--accent);
    font-size: 25px;
    letter-spacing: .3px;
    line-height: 1.1;
  }
  .office-address { margin-top: 8px; font-size: 19px; line-height: 1.35; color: var(--ink); }
  .office-note { margin-top: auto; padding-bottom: 20px; font-size: 11px; color: var(--ink-soft); text-align: right; }

  /* Back */
  .card-back { left: 510px; top: 345px; width: 630px; height: 380px; }
  .handle-band {
    position: absolute; left: 0; right: 0; top: 90px; height: 100px;
    background: var(--card-band);
    display: flex; align-items: center; justify-content: center; gap: 16px;
  }
  .handle-mark { width: 34px; height: 34px; flex: none; }
  .handle { font-size: 22px; color: var(--ink); letter-spacing: .5px; }
  .back-brand {
    position: absolute; left: 0; right: 0; top: 240px;
    text-align: center;
    font-size: 46px; letter-spacing: 10px;
  }
</style>
</head>
<body>
  <article class="card card-front">
    <div class="portrait" role="img" aria-label="Portrait photo of Marvin Pold in a grey blazer in front of a leafy garden wall"></div>
    <div class="front-brand">
      <div class="brand-name">MPold Realty</div>
      <div class="agent-name">Marvin Pold</div>
      <div class="agent-title">Broker/Owner</div>
      <div class="phones">
        <div>555-210-3367</div>
        <div>555-384-9021</div>
      </div>
    </div>
    <div class="web-band">
      <div>Marvin@MPoldRealty.com</div>
      <div>www.MPoldRealty.com</div>
    </div>
    <div class="office">
      <div class="office-title">Linwood Area Market Center</div>
      <div class="office-address">
        <div>1875 Harlow Lane, Suite 204</div>
        <div>Ashford, NC 20415</div>
      </div>
      <div class="office-note">Each office is Independently Owned &amp; Operated</div>
    </div>
  </article>

  <article class="card card-back">
    <div class="handle-band">
      <svg class="handle-mark" viewBox="0 0 34 34" aria-hidden="true">
        <circle cx="17" cy="17" r="14" fill="none" stroke="var(--accent)" stroke-width="3"/>
      </svg>
      <span class="handle">the_pinecrest_realtor</span>
    </div>
    <div class="brand-name back-brand">MPold Realty</div>
  </article>
</body>
</html>
```